Professional individual needs business card design

I need a business card designed for my friend to show their skills and contact details

I would like to see pattern designs with a black foreground and strong look - will submit content specifics but basics are:

NAME SURNAME (large and bold)
Event Manager & MC

Velvet Harbour
The other event I run

phone number - email

```html
<!DOCTYPE html>
<html lang="en">
<head>
<meta charset="utf-8">
<title>Business Card – Event Manager &amp; MC</title>
<link rel="stylesheet" href="https://fonts.googleapis.com/css2?family=Source+Sans+3:wght@400;600;700&display=swap">
<style>
  :root {
    --page-bg: #141414;
    --card-bg: #262626;
    --accent: #7cb82f;
    --text-light: #ececec;
    --font-main: "Source Sans 3", sans-serif;
  }
  html, body {
    margin: 0;
    padding: 0;
    width: 1200px;
    height: 1001px;
    overflow: hidden;
    background: var(--page-bg);
    font-family: var(--font-main);
  }
  .business-card {
    position: absolute;
    left: 100px;
    top: 215px;
    width: 1000px;
    height: 571px;
    background: var(--card-bg);
    box-shadow: 0 10px 40px rgba(0,0,0,0.6);
  }
  .person {
    position: absolute;
    left: 510px;
    top: 62px;
  }
  .person-name {
    margin: 0;
    font-size: 40px;
    font-weight: 700;
    letter-spacing: 0.5px;
    color: var(--accent);
    line-height: 1;
  }
  .person-role {
    margin: 10px 0 0;
    font-size: 23px;
    color: var(--text-light);
  }
  .divider {
    position: absolute;
    top: 272px;
    height: 3px;
    background: var(--accent);
  }
  .divider-left { left: 0; width: 82px; }
  .divider-right { left: 510px; right: 0; }
  .brand {
    position: absolute;
    left: 104px;
    top: 242px;
    display: flex;
    align-items: center;
    gap: 12px;
    font-size: 48px;
    font-weight: 400;
    color: var(--accent);
    line-height: 1;
  }
  .brand-dot {
    width: 14px;
    height: 14px;
    border-radius: 50%;
    background: var(--accent);
  }
  .address {
    position: absolute;
    left: 512px;
    top: 318px;
    margin: 0;
    font-size: 24px;
    line-height: 1.35;
    font-style: normal;
    color: var(--text-light);
  }
  .contact-list {
    position: absolute;
    left: 512px;
    top: 412px;
    margin: 0;
    padding: 0;
    list-style: none;
    font-size: 24px;
    color: var(--text-light);
  }
  .contact-list li {
    display: flex;
    align-items: center;
    gap: 14px;
    height: 31px;
  }
  .contact-icon {
    width: 20px;
    height: 20px;
    fill: var(--accent);
    flex: none;
  }
</style>
</head>
<body>
  <section class="business-card">
    <div class="person">
      <h1 class="person-name">NAME SURNAME</h1>
      <p class="person-role">Event Manager &amp; MC</p>
    </div>

    <div class="divider divider-left"></div>
    <div class="brand"><span>Velvet Harbour</span><span class="brand-dot"></span></div>
    <div class="divider divider-right"></div>

    <address class="address">P.O. Box: 1234, Linden Row,<br>London, United Kingdom</address>

    <ul class="contact-list">
      <li>
        <svg class="contact-icon" viewBox="0 0 20 20" aria-hidden="true"><path d="M2 6c0-2 3-3 8-3s8 1 8 3v2h-4V6H6v2H2z"/><path d="M4 9h12l1 8H3z"/></svg>
        <span>Tel: 0099 5550142786</span>
      </li>
      <li>
        <svg class="contact-icon" viewBox="0 0 20 20" aria-hidden="true"><rect x="5" y="2" width="10" height="5"/><rect x="2" y="8" width="16" height="7" rx="1"/><rect x="5" y="13" width="10" height="5"/></svg>
        <span>Fax: 0099 5550142787</span>
      </li>
      <li>
        <svg class="contact-icon" viewBox="0 0 20 20" aria-hidden="true"><path d="M2 4h16v12H2z M3 5l7 6 7-6" /><path d="M3 5l7 6 7-6" fill="none" stroke="#262626" stroke-width="1.5"/></svg>
        <span>Email: info@velvetharbour.com</span>
      </li>
      <li>
        <svg class="contact-icon" viewBox="0 0 20 20" aria-hidden="true"><circle cx="10" cy="10" r="8"/><g fill="none" stroke="#262626" stroke-width="1.2"><ellipse cx="10" cy="10" rx="3.5" ry="8"/><path d="M2 10h16M3.5 6h13M3.5 14h13"/></g></svg>
        <span>Web: www.velvetharbour.com</span>
      </li>
    </ul>
  </section>
</body>
</html>
```